Business Cards for cafe providing speciality coffee and food

I need a business card design for my husband’s businesses. He has two cafes in Brisbane. The business name is Copperleaf Roasting House. They sell high end specialty coffee as well as breakfast and lunch. All the food is cooked fresh, in house and they have strict quality controls for their coffee. I would like the business card to feature the address for both cafes, my husband’s phone number and the business’s instagram. The address for the first is 61 Walden Crescent, Oakvale and the second is 23 Pellow Avenue, Brindlemoor. The Instagram handle is @copperleafroastinghouse and phone number is 0491362847. We already have a business logo that is attached.

Target Market(s)

All ages, higher disposable income and more likely to eat out regularly

Industry/Entity Type

Hospitality

Contact Information for Business Card

Must be suitable for both customers and suppliers

Font styles to use
Sans Serif

Colors

Designer to choose colors to be used in the design.

Requirements
Must have
• Owner’s name: Reid Castell
• Addresses of both cafes: 61 Walden Crescent, Oakvale and 23 Pellow Avenue, Brindlemoor
• Instagram handle: @copperleafroastinghouse
• Contact number: 0491362847
Nice to have
• Business logo

```html
<!DOCTYPE html>
<html lang="en">
<head>
<meta charset="utf-8">
<title>Copperleaf Roasting House – Business Cards</title>
<link href="https://fonts.googleapis.com/css2?family=Source+Sans+3:wght@400;700&display=swap" rel="stylesheet">
<style>
  :root {
    --backdrop: #2b2b2b;
    --card: #141414;
    --ink: #f2f2f2;
    --silver: #b9b9b9;
    --band: #ffffff;
  }
  * { margin: 0; padding: 0; box-sizing: border-box; }
  html, body { width: 1200px; height: 900px; overflow: hidden; }
  body {
    background: var(--backdrop);
    font-family: "Source Sans 3", "Myriad Pro", Arial, sans-serif;
    color: var(--ink);
    position: relative;
  }
  .card {
    position: absolute;
    left: 250px;
    width: 700px;
    height: 400px;
    background: var(--card);
    overflow: hidden;
  }
  .card--back { top: 30px; }
  .card--front { top: 470px; }

  .brand-mark {
    position: absolute;
    display: flex;
    align-items: center;
    justify-content: center;
    text-align: center;
    border-radius: 50%;
  }
  .card--back .brand-mark {
    width: 190px; height: 190px;
    left: 255px; top: 105px;
    border: 3px solid var(--silver);
    color: var(--silver);
    font-weight: 700;
    font-size: 22px;
    line-height: 1.15;
    letter-spacing: 1px;
    text-transform: uppercase;
  }
  .card--front .brand-mark {
    width: 160px; height: 160px;
    left: 500px; top: 28px;
    border: 3px solid var(--ink);
    color: var(--ink);
    font-weight: 700;
    font-size: 18px;
    line-height: 1.15;
    letter-spacing: 1px;
    text-transform: uppercase;
  }

  .owner-name {
    position: absolute;
    left: 60px; top: 200px;
    font-size: 24px;
    font-weight: 700;
    letter-spacing: 0.5px;
    text-transform: uppercase;
  }
  .divider {
    position: absolute;
    left: 60px; right: 40px; top: 245px;
    height: 2px;
    background: var(--ink);
  }
  .addresses {
    position: absolute;
    left: 60px; top: 258px;
    font-size: 17px;
    line-height: 1.3;
  }
  .contact-list {
    position: absolute;
    left: 440px; top: 192px;
    list-style: none;
    font-size: 17px;
    line-height: 1.45;
  }
  .contact-list li { display: flex; align-items: center; gap: 10px; }
  .contact-list svg { width: 14px; height: 14px; flex: none; }
  .social-square {
    width: 13px; height: 13px;
    border: 2px solid var(--ink);
    flex: none;
  }
  .bottom-band {
    position: absolute;
    left: 0; right: 0; bottom: 0;
    height: 14px;
    background: var(--band);
  }
</style>
</head>
<body>
  <section class="card card--back" aria-label="Business card back">
    <div class="brand-mark">Copperleaf<br>Roasting<br>House</div>
  </section>

  <section class="card card--front" aria-label="Business card front">
    <div class="brand-mark">Copperleaf<br>Roasting<br>House</div>

    <h1 class="owner-name">Reid Castell</h1>

    <ul class="contact-list">
      <li>
        <svg viewBox="0 0 24 24" aria-hidden="true"><path fill="#f2f2f2" d="M6.6 10.8a15.2 15.2 0 0 0 6.6 6.6l2.2-2.2a1 1 0 0 1 1-.25 11.4 11.4 0 0 0 3.6.57 1 1 0 0 1 1 1V20a1 1 0 0 1-1 1A17 17 0 0 1 3 4a1 1 0 0 1 1-1h3.5a1 1 0 0 1 1 1c0 1.25.2 2.45.57 3.57a1 1 0 0 1-.25 1z"/></svg>
        <span>0491362847</span>
      </li>
      <li>
        <span class="social-square"></span>
        <span>@copperleafroastinghouse</span>
      </li>
    </ul>

    <div class="divider"></div>

    <address class="addresses" style="font-style: normal;">
      61 Walden Crescent<br>
      Oakvale and 23 Pellow Avenue<br>
      Brindlemoor
    </address>

    <div class="bottom-band"></div>
  </section>
</body>
</html>
```